RLTP Business Card Design

I have a rough idea of the design / layout of the company business card but need help in finalizing the design and quality.

I'm looking for the card to be stand out, but simple, on the front with clear detail on the back with space for some one to write any other detail they need onto the card. The rough draft includes the crinkled graph paper back ground which I quite like for the front.

I will need the card design completed and ready to print in Australian business card standard sizes. This includes detail on all colors, fonts and type faces used as well as copy of the original for editing (inserting other employee details).

I have included the company logo and a rough draft of the card, including the graphic I would like to use for the back ground on the front, I am not sure that the graphic is any good for printing, not the highest res.

Thanks,

Owen

```html
<!DOCTYPE html>
<html lang="en">
<head>
<meta charset="utf-8">
<title>RLTP Business Card</title>
<link href="https://fonts.googleapis.com/css2?family=Michroma&display=swap" rel="stylesheet">
<style>
  :root {
    --page-bg: #e6e6e4;
    --card-top: #ffffff;
    --card-bottom: #ebebeb;
    --ink: #141414;
    --ink-soft: #3a3a3a;
    --swoosh-black: #0c0c0c;
    --swoosh-grey: #8d8d8d;
    --rule: #2a2a2a;
  }
  * { box-sizing: border-box; margin: 0; padding: 0; }
  html, body {
    width: 1200px; height: 900px; overflow: hidden;
    background: var(--page-bg);
    font-family: "Michroma", sans-serif;
    color: var(--ink);
  }
  .card {
    position: absolute; left: 150px; top: 175px;
    width: 900px; height: 550px;
    border-radius: 46px; overflow: hidden;
    background: linear-gradient(160deg, var(--card-top) 35%, var(--card-bottom) 100%);
    box-shadow: 0 18px 40px rgba(0,0,0,0.18);
  }
  .card-swoosh { position: absolute; inset: 0; width: 900px; height: 550px; }
  .brand {
    position: absolute; left: 250px; top: 92px; width: 440px;
  }
  .brand-name {
    font-size: 104px; line-height: 1; letter-spacing: 2px; color: var(--ink);
  }
  .brand-tagline {
    margin-top: 8px; font-size: 13.5px; letter-spacing: 1.4px;
    text-transform: uppercase; color: var(--ink);
  }
  .divider {
    position: absolute; left: 478px; top: 262px; width: 1.5px; height: 190px;
    background: var(--rule);
  }
  .person {
    position: absolute; right: 442px; top: 292px; text-align: right;
    font-variant: small-caps; color: var(--ink);
  }
  .person-name { font-size: 19px; letter-spacing: 1.5px; }
  .person-role { font-size: 15px; letter-spacing: 1.2px; margin-top: 6px; color: var(--ink-soft); }
  .address { margin-top: 44px; font-size: 16px; letter-spacing: 1.4px; line-height: 1.6; }
  .contacts {
    position: absolute; left: 500px; top: 262px; list-style: none;
    font-size: 17px; letter-spacing: 1.6px; color: var(--ink);
  }
  .contacts li { display: flex; align-items: center; gap: 10px; height: 27px; }
  .contacts li.gap-before { margin-top: 14px; }
  .contacts li.lower { font-variant: small-caps; font-size: 15.5px; }
  .contact-icon { width: 16px; height: 16px; flex: none; }
</style>
</head>
<body>
  <main class="card" aria-label="RLTP business card front">
    <svg class="card-swoosh" viewBox="0 0 900 550" aria-hidden="true">
      <path d="M0 95 C 30 260, 130 430, 300 550 L 0 550 Z" fill="var(--swoosh-black)"/>
      <path d="M28 160 C 80 330, 200 470, 360 550 L 300 550 C 150 450, 60 320, 28 160 Z" fill="var(--swoosh-grey)"/>
    </svg>

    <header class="brand">
      <div class="brand-name">RLTP</div>
      <div class="brand-tagline">Real Live Tech Productions .com.au</div>
    </header>

    <section class="person">
      <div class="person-name">Owen Harker</div>
      <div class="person-role">Owner / C.E.O</div>
      <div class="address">Suite # 14, Kent House,<br>NSW 2041</div>
    </section>

    <div class="divider"></div>

    <ul class="contacts">
      <li>
        <svg class="contact-icon" viewBox="0 0 16 16" aria-hidden="true"><circle cx="8" cy="8" r="8" fill="var(--ink)"/><path d="M5 4.5l2 1.6-1 1.4c.6 1.2 1.4 2 2.6 2.6l1.4-1 1.6 2-1.2 1.2c-3-.6-5.5-3.1-6.1-6.1z" fill="#fff"/></svg>
        402-318-5561
      </li>
      <li>
        <svg class="contact-icon" viewBox="0 0 16 16" aria-hidden="true"><circle cx="8" cy="8" r="8" fill="var(--ink)"/><rect x="5.5" y="3.5" width="5" height="9" rx="1" fill="#fff"/><rect x="6.5" y="4.8" width="3" height="5.5" fill="var(--ink)"/></svg>
        417-926-0384
      </li>
      <li>
        <svg class="contact-icon" viewBox="0 0 16 16" aria-hidden="true"><circle cx="8" cy="8" r="8" fill="var(--ink)"/><rect x="4" y="6.5" width="8" height="5" rx="0.8" fill="#fff"/><rect x="5.5" y="4" width="5" height="3" fill="#fff"/></svg>
        403-771-2049
      </li>
      <li class="gap-before lower">
        <svg class="contact-icon" viewBox="0 0 16 16" aria-hidden="true"><circle cx="8" cy="8" r="8" fill="var(--ink)"/><rect x="4" y="5" width="8" height="6" rx="0.6" fill="#fff"/><path d="M4.3 5.3L8 8.4l3.7-3.1" fill="none" stroke="var(--ink)" stroke-width="0.9"/></svg>
        owen@rltpstudio.com
      </li>
      <li class="lower">
        <svg class="contact-icon" viewBox="0 0 16 16" aria-hidden="true"><circle cx="8" cy="8" r="8" fill="var(--ink)"/><circle cx="8" cy="8" r="4.2" fill="none" stroke="#fff" stroke-width="1"/><path d="M3.8 8h8.4M8 3.8c-2 2.5-2 5.9 0 8.4M8 3.8c2 2.5 2 5.9 0 8.4" fill="none" stroke="#fff" stroke-width="0.8"/></svg>
        www.rltpstudio.com
      </li>
    </ul>
  </main>
</body>
</html>
```